Retractable Banner Design Featuring Key Product for Beauty Trade Show

We're a beauty/nail supply company that specializes in products used in professional nail salons. The key product for this design is Disposable Latex Gloves.
We will be exhibiting in a trade show this summer and are looking for a free-standing Retractable Banner Design that will be displayed at the front of our booth. The goal of the banner will be to display key products that are high in demand with our customers. The banner will be used to attract attention and highlight key selling points of these popular products. We would like the banner to be focused on the product title, image and key points, with a beauty/model/pattern background to create a professional appearance.
Nail Salons
Nail & Beauty Industry

```html
<!DOCTYPE html>
<html lang="en">
<head>
<meta charset="utf-8">
<title>Latex Gloves – Retractable Banner</title>
<link href="https://fonts.googleapis.com/css2?family=Bebas+Neue&family=Oswald:wght@300&family=Open+Sans:wght@600;700&display=swap" rel="stylesheet">
<style>
  :root {
    --orange: #e8740c;
    --orange-light: #f7962f;
    --orange-deep: #e06a08;
    --grey-wedge: #7a7a7a;
    --ink: #3a3a3a;
    --paper: #ffffff;
    --paper-shade: #eeeeee;
    --stage: #e9eef3;
  }
  * { margin: 0; padding: 0; box-sizing: border-box; }
  html, body { width: 1200px; height: 2432px; overflow: hidden; background: var(--stage); }
  .banner {
    position: absolute; left: 100px; top: 40px;
    width: 1000px; height: 2352px;
    background: linear-gradient(90deg, var(--paper-shade) 0%, var(--paper) 40%, var(--paper) 100%);
    overflow: hidden;
  }
  .title {
    position: absolute; left: 90px; top: 50px;
    font-family: "Bebas Neue", sans-serif;
    color: var(--orange);
    font-size: 282px; line-height: 250px;
    letter-spacing: 2px;
  }
  .pack-info {
    position: absolute; left: 94px; top: 575px;
    font-family: "Oswald", sans-serif; font-weight: 300;
    color: var(--ink); font-size: 64px; line-height: 88px;
  }
  .key-head { position: absolute; left: 100px; top: 789px; width: 780px; height: 66px; }
  .key-head .rule { position: absolute; left: 0; bottom: 0; width: 100%; height: 3px; background: var(--orange); }
  .key-head .tag {
    position: absolute; left: 0; top: 0; width: 325px; height: 66px;
    background: var(--orange);
    clip-path: polygon(0 0, 86% 0, 100% 100%, 0 100%);
    font-family: "Open Sans", sans-serif; font-weight: 700;
    color: var(--paper); font-size: 38px; line-height: 66px; padding-left: 22px;
  }
  .points { position: absolute; left: 110px; top: 888px; list-style: none; }
  .points li {
    display: flex; align-items: center; gap: 18px;
    font-family: "Open Sans", sans-serif; font-weight: 600;
    color: var(--ink); font-size: 33px; height: 64px;
  }
  .points svg { width: 28px; height: 28px; flex: none; }
  .backdrop { position: absolute; left: 0; top: 0; width: 1000px; height: 2352px; }
  .product-shot {
    position: absolute; left: 374px; top: 1175px; width: 585px; height: 355px;
    background: linear-gradient(135deg, #fafafa 0%, #f1f1f1 45%, var(--orange) 46%, var(--orange-deep) 100%);
    border-radius: 6px;
  }
  .hands-shot {
    position: absolute; left: 230px; top: 1580px; width: 770px; height: 772px;
    background: radial-gradient(ellipse at 45% 45%, #f4f2f0 0%, #e9e4df 40%, rgba(240,190,150,0.6) 62%, rgba(232,116,12,0) 80%);
  }
</style>
</head>
<body>
  <main class="banner">
    <svg class="backdrop" viewBox="0 0 1000 2352" aria-hidden="true">
      <defs>
        <linearGradient id="orangeFill" x1="0" y1="0" x2="1" y2="1">
          <stop offset="0" stop-color="#f9a23c"/>
          <stop offset="1" stop-color="#e8740c"/>
        </linearGradient>
      </defs>
      <polygon points="0,1296 400,1512 0,1626" fill="var(--grey-wedge)"/>
      <polygon points="0,1626 1000,1336 1000,2352 0,2352" fill="url(#orangeFill)"/>
    </svg>

    <h1 class="title">LATEX<br>GLOVES</h1>
    <p class="pack-info">(1,000 PCS/CASE)<br>(84 CASES PER PALLET)</p>

    <div class="key-head">
      <div class="rule"></div>
      <div class="tag">KEY POINTS:</div>
    </div>

    <ul class="points">
      <li><svg viewBox="0 0 28 28"><rect x="2" y="2" width="24" height="24" fill="none" stroke="#e8740c" stroke-width="3"/><path d="M7 14l5 5 10-12" fill="none" stroke="#e8740c" stroke-width="3"/></svg>100% Powder-Free – no residue or irritants</li>
      <li><svg viewBox="0 0 28 28"><rect x="2" y="2" width="24" height="24" fill="none" stroke="#e8740c" stroke-width="3"/><path d="M7 14l5 5 10-12" fill="none" stroke="#e8740c" stroke-width="3"/></svg>Premium Textured Grip for Superior Grip</li>
      <li><svg viewBox="0 0 28 28"><rect x="2" y="2" width="24" height="24" fill="none" stroke="#e8740c" stroke-width="3"/><path d="M7 14l5 5 10-12" fill="none" stroke="#e8740c" stroke-width="3"/></svg>6.2g Latex – Super Heavy Duty</li>
      <li><svg viewBox="0 0 28 28"><rect x="2" y="2" width="24" height="24" fill="none" stroke="#e8740c" stroke-width="3"/><path d="M7 14l5 5 10-12" fill="none" stroke="#e8740c" stroke-width="3"/></svg>Designed for Professional Salons!</li>
    </ul>

    <div class="product-shot" role="img" aria-label="Photo of latex glove boxes: a small dispenser box in front of a larger orange case"></div>
    <div class="hands-shot" role="img" aria-label="Photo of hands pulling on white latex gloves"></div>
  </main>
</body>
</html>
```